Business Card Design Project

for a second hand vintage clothing store. shop name is The Velvet Loft

Cards to be double sided

The name on the card is Marianne Trelford

Information to put on card:

The Velvet Loft
Marianne Trelford (no job title)
84/227 Quayle St, Pyrmont, Sydney, NSW, 2009.
Mobile: 0412 975 206
Email: thevelvetloft@mailbox-example.com.au
Web: www.thevelvetloft-example.com.au

Target Market(s)

Women looking at vintage clothing

Industry/Entity Type

Clothing

```html
<!DOCTYPE html>
<html lang="en">
<head>
<meta charset="utf-8">
<title>The Velvet Loft – Business Card</title>
<link rel="stylesheet" href="https://fonts.googleapis.com/css2?family=Questrial&display=swap">
<style>
  :root {
    --page: #ffffff;
    --card: #5a2433;
    --cream: #f0d79a;
    --white: #f3ece8;
    --muted: #b99a9e;
    --label: #111111;
  }
  * { margin: 0; padding: 0; box-sizing: border-box; }
  html, body {
    width: 1200px;
    height: 1200px;
    overflow: hidden;
    background: var(--page);
    font-family: "Questrial", sans-serif;
  }
  .canvas {
    position: relative;
    width: 1200px;
    height: 1200px;
  }
  .side-label {
    position: absolute;
    left: 0;
    width: 1200px;
    text-align: center;
    font-size: 18px;
    color: var(--label);
  }
  .side-label--back { top: 44px; }
  .side-label--front { top: 546px; }

  .card {
    position: absolute;
    left: 130px;
    width: 928px;
    height: 462px;
    background: var(--card);
  }
  .card--back { top: 68px; }
  .card--front { top: 585px; }

  .brand-name {
    position: absolute;
    color: var(--cream);
    font-family: "Questrial", sans-serif;
    white-space: nowrap;
    line-height: 1;
  }
  .card--back .brand-name {
    right: 40px;
    top: 52px;
    font-size: 54px;
  }
  .card--front .brand-name {
    right: 62px;
    top: 300px;
    font-size: 60px;
  }

  .holder {
    position: absolute;
    left: 34px;
    top: 262px;
  }
  .holder-name {
    font-size: 39px;
    letter-spacing: 7px;
    line-height: 1;
    white-space: nowrap;
  }
  .holder-name .first { color: var(--white); }
  .holder-name .last { color: var(--cream); }
  .holder-address {
    text-align: right;
    font-size: 13px;
    color: var(--white);
    margin-top: 8px;
    padding-right: 6px;
    white-space: nowrap;
  }

  .contact-list {
    position: absolute;
    left: 36px;
    top: 342px;
    list-style: none;
  }
  .contact-line {
    font-size: 15px;
    line-height: 22px;
    color: var(--muted);
    white-space: nowrap;
  }
  .contact-line .accent { color: var(--cream); }

  .contact-phone {
    position: absolute;
    left: 34px;
    top: 400px;
    font-size: 29px;
    letter-spacing: 5px;
    white-space: nowrap;
    line-height: 1.2;
  }
  .contact-phone .prefix { color: var(--white); }
  .contact-phone .number { color: var(--cream); }
</style>
</head>
<body>
<main class="canvas">
  <p class="side-label side-label--back">Back side</p>
  <section class="card card--back" aria-label="Card back">
    <div class="brand-name">The Velvet Loft</div>
    <div class="holder">
      <p class="holder-name"><span class="first">Marianne</span> <span class="last">Trelford</span></p>
      <p class="holder-address">84/227 Quayle St, Pyrmont, Sydney, NSW, 2009</p>
    </div>
    <ul class="contact-list">
      <li class="contact-line">thevelvetloft<span class="accent">@mailbox-example.com.au</span></li>
      <li class="contact-line">www.<span class="accent">thevelvetloft-example.com.au</span></li>
    </ul>
    <p class="contact-phone"><span class="prefix">M </span><span class="number">0412 975 206</span></p>
  </section>

  <p class="side-label side-label--front">Front side</p>
  <section class="card card--front" aria-label="Card front">
    <div class="brand-name">The Velvet Loft</div>
  </section>
</main>
</body>
</html>
```